【 概要 】 小児科病棟訪問・特別支援学校訪問などの社会貢献活動「https://movu-hop.jp」に取り組んできました。 その活動の中で課題を感じる様になりました。 『この子たちの、この先の人生に寄与することはできないか』 そんなか障害を抱えるお子さんを持つ親御さんから、 「18歳までは(特別支援学校があるから)社会的な居場所があるけど、18際を過ぎた途端、急に居場所がなくなるんですよね」 と聞きました。 社会貢献活動をしたいと思っていたのに、そんな事も知らなかったのかと恥じました。 知ったからには行動しよう! そして多くの方のご意見をいただき、障害者就労継続支援B型事業所を開所することとなりました。 <参考> いくつかあるメディア掲載記事をご覧ください。 https://www.hiyorinews-daily.jp/article/KTRWMBXE47BNK3T8B511D7000000/ https://www.vidoramatube.com/watch?v=Tq8kPwn41Lc https://takibi-fundr.jp/projects/view/781246 【会社名】 株式会社Movu Lane 【事業所名】 Movu Garden さいたま 【キャッチコピー】 笑顔でつなぐ、未来への道 【 依頼内容 】 ・サイズ:A4 両面 3つ折り仕様 ・ページ数:1ページ ・素材の用意(画像・文章等):会社ロゴ・代表宣材写真・養蜂の様子は用意します。その他必要な写真があれば可能な範囲でお応えします。 ・デザイン内容:利用者さんの集客や仕事の受注につながる様なデザイン 【掲載内容】 ●表紙 ●あいさつ(概要) ●ご利用までの流れ ①問い合わせ →まずは、お電話かメールにてお問い合わせください。 ②見学 →事業所の雰囲気をご覧いただき、スタッフとお話ししてみてください。 ③体験実習 →3日から1週間程度、ご都合に合わせて通っていただきます。 ④利用開始 →利用契約を結び、正式に利用開始となります。 ●対象 65歳未満で就労の意思があり、『障害福祉サービス受給者証』をお持ちの方です。 ●利用料金 原則1割負担ですが、多くの場合は無料でご利用いただけます。受給者証の取得など、必要であればお手伝いいたします。 ●利用開始前に 見学→体験実習をおすすめします。ご自身に合うか確かめてからご利用ください。 ●作業内容 ・養蜂 →障がい者の就労機会の創出と地域交流の促進につながるプロジェクトになることが期待されます。(見沼区地域にて作業) ・コーヒー豆 →生豆の中に数パーセント含まれる、形や大きさが不揃いな豆や青カビが付着した豆を丁寧に取り除いていきます。 その後梱包・発送まで担います。 ・古本ネット販売 →回収した本の仕分け、清掃、出品、梱包、配送など、ネット通販を行います。 ●アクセス ●お問い合わせ 【 デザインイメージ 】 ・ターゲット層:障害を持つ方、またそのご家族。障害者雇用に関心のある企業の方。 ・雰囲気:親しみやすくおしゃれな雰囲気 【 契約金額(税抜) 】 3万円 ※上記記載内容をベースとし、柔軟に編集いただければと思います。(表記の仕方などはお任せします) ※契約金額(税込)からシステム利用料を差し引いた金額が、ワーカーさまの受取金額となります。 その他ご質問等ありましたら、気軽にお問い合わせください。 写真などの素材も必要であれば、お問い合わせください。 ご応募をお待ちしております! |
色使いやレイアウト等、事業所の理念や私(代表)の想い通りのデザインをしていただきました。
また、度重なる細かい修正依頼にもスピーディーに快く引き受けてくださいました。
皆様たくさんのご提案をいただきありがとうございました。
どれも素敵なデザインで選定するのが非常に困難でした。
十分な報酬をお支払いできないにも関わらず、たくさんのご提案をいただけたこと大変感謝申し上げます。
引き続き弊社の活動を応援していただけますと幸いに存じます。

```html
<!DOCTYPE html>
<html lang="ja">
<head>
<meta charset="utf-8">
<title>ご利用案内</title>
<link rel="stylesheet" href="https://fonts.googleapis.com/css2?family=M+PLUS+Rounded+1c:wght@400;500;700;800&display=swap">
<style>
:root{
  --bg:#f7d3e2;
  --pink:#e5508a;
  --pink-soft:#f5c2d6;
  --ink:#3a3a3a;
  --muted:#666;
  --paper:#ffffff;
  --lavender:#ece6f3;
  --mint:#e6f2df;
  --red:#e2404f;
  --orange:#ef7b2d;
  --green:#8cbc3f;
  --yellow:#fff06a;
}
*{box-sizing:border-box;margin:0;padding:0}
html,body{width:1200px;height:856px;overflow:hidden}
body{background:var(--bg);font-family:"M PLUS Rounded 1c",sans-serif;color:var(--ink);position:relative}
.abs{position:absolute}
.main-sheet{left:10px;top:14px;width:800px;height:830px;background:var(--paper);clip-path:polygon(2% 4%,30% 0,60% 2%,98% 1%,100% 40%,97% 100%,50% 98%,0 100%,1% 50%)}
.illust{border-radius:18px}
.faces{left:300px;top:18px;width:470px;height:76px;background:linear-gradient(90deg,#f9d8b8,#f6c7a0,#e9d3c1)}
.crowd{left:24px;top:560px;width:250px;height:270px;background:linear-gradient(180deg,#f7c9a3,#f29fb8 60%,#9dc9ea)}
.family{left:870px;top:630px;width:280px;height:170px;background:linear-gradient(180deg,#d9efc6,#f3c1a6,#c3a4d8)}
.tape{height:22px;opacity:.85}
.card{padding-top:30px;text-align:center}
.target{left:100px;top:170px;width:320px;height:250px;background:var(--lavender);transform:rotate(-1deg)}
.fee{left:450px;top:175px;width:330px;height:235px;background:var(--mint);transform:rotate(1deg)}
.card-title{font-size:26px;font-weight:700;letter-spacing:.1em;color:var(--ink)}
.fee .card-title{display:inline-block;background:#fff;color:var(--ink);padding:2px 18px;border-radius:8px}
.target ul{list-style:none;text-align:left;margin:22px 0 0 34px;font-size:17px;font-weight:700;line-height:1.35}
.target li{margin-bottom:12px}
.note{font-size:12px;color:var(--muted);line-height:1.5}
.target .note{text-align:left;margin-left:34px}
.fee-main{font-size:19px;font-weight:700;margin:22px 0 14px}
.fee .note{text-align:left;margin-left:74px}
.free{color:var(--red);font-weight:800;font-size:17px}
.work-title{left:410px;top:428px;font-size:26px;font-weight:700;letter-spacing:.1em}
.work-lead{left:272px;top:468px;font-size:13px;font-weight:700;color:var(--orange);background:linear-gradient(transparent 50%,var(--yellow) 50%)}
.speech{left:112px;top:458px;font-size:14px;font-weight:700;line-height:1.4;transform:rotate(-6deg)}
.job{background:#fff;border-radius:10px;box-shadow:0 2px 8px rgba(0,0,0,.12);padding:34px 16px 10px;font-size:12px;line-height:1.6;color:var(--muted)}
.job-label{position:absolute;top:-14px;left:14px;color:#fff;font-weight:700;font-size:15px;padding:3px 14px;border-radius:4px}
.book{left:272px;top:514px;width:280px;height:110px}
.book .job-label{background:var(--red)}
.coffee{left:566px;top:510px;width:220px;height:110px}
.coffee .job-label{background:var(--orange)}
.bee{left:494px;top:634px;width:296px;height:124px}
.bee .job-label{background:var(--green)}
.flow-panel{left:826px;top:20px;width:354px;height:816px;background:#fff;border-radius:14px}
.flow-title{left:866px;top:38px;font-size:24px;font-weight:700;color:var(--pink);letter-spacing:.05em}
.step{left:846px;width:320px}
.step-head{display:flex;align-items:baseline;gap:14px;border-bottom:2px solid var(--pink-soft);padding-bottom:3px}
.step-no{font-size:14px;font-weight:700;color:var(--pink);font-style:normal}
.step-name{font-size:18px;font-weight:700;color:var(--pink)}
.step p{font-size:12px;color:var(--muted);margin-top:8px;line-height:1.5}
.before{left:852px;top:450px;width:300px;height:92px;background:var(--pink-soft);border-radius:46px;padding:18px 34px;font-size:12px;line-height:1.6;color:var(--ink)}
.before-title{left:934px;top:432px;font-size:17px;font-weight:700;color:var(--pink);background:#fff;padding:0 8px;border-radius:8px}
.bulb{left:866px;top:402px}
</style>
</head>
<body>
<div class="abs main-sheet"></div>

<div class="abs illust faces" role="img" aria-label="笑顔の人々の顔のイラストが横に並ぶ"></div>

<div class="abs tape" style="left:70px;top:140px;width:130px;background:#c8a6e6;transform:rotate(-28deg)"></div>
<div class="abs tape" style="left:380px;top:188px;width:110px;background:#f2a6a0;transform:rotate(-35deg)"></div>
<div class="abs tape" style="left:690px;top:150px;width:110px;background:#9ecfee;transform:rotate(30deg)"></div>
<div class="abs tape" style="left:740px;top:420px;width:90px;background:#7ab7ee;transform:rotate(-40deg)"></div>
<div class="abs tape" style="left:560px;top:490px;width:80px;background:#fbe27a;transform:rotate(8deg)"></div>

<section class="abs card target">
  <h2 class="card-title">対象</h2>
  <ul>
    <li>65歳未満で就労の意思がある方</li>
    <li>障害福祉サービス受給者証<br>をお持ちの方</li>
  </ul>
  <p class="note">※必要であれば受給者証の取得<br>などのお手伝いも致します。</p>
</section>

<section class="abs card fee">
  <h2 class="card-title">利用料金</h2>
  <p class="fee-main">原則1割負担</p>
  <p class="note">※多くの場合は<span class="free">無料</span>で<br>ご利用いただけます。<br>詳しくはご相談ください。</p>
</section>

<p class="abs speech">楽しそうなお仕事が<br>いっぱいだね！</p>
<h2 class="abs work-title">作業内容</h2>
<p class="abs work-lead">障がい者の就労機会の創出と地域交流の促進につながるプロジェクトです！</p>

<div class="abs illust crowd" role="img" aria-label="さまざまな年代の人々と犬が並ぶイラスト"></div>

<article class="abs job book">
  <span class="job-label">古本ネット販売</span>
  回収した本の仕分け・清掃から、出品・梱包配送などをネット通販を通して行います。
</article>
<article class="abs job coffee">
  <span class="job-label">コーヒー豆</span>
  生豆の中に含まれる形や大きさが不揃いな豆や青カビが付着した豆を取り除く作業です。
</article>
<article class="abs job bee">
  <span class="job-label">養蜂</span>
  見沼区地域にて「養蜂箱」と呼ばれる木箱の中でミツバチのお世話をし、採蜜します。ミツバチはめったに刺さないハチなので心配には及びません。
</article>

<div class="abs flow-panel"></div>
<h2 class="abs flow-title">ご利用までの流れ</h2>

<div class="abs step" style="top:106px">
  <div class="step-head"><em class="step-no">step.1</em><span class="step-name">お問い合せ</span></div>
  <p>まずは、お電話かメールにてお問い合わせください。</p>
</div>
<div class="abs step" style="top:176px">
  <div class="step-head"><em class="step-no">step.2</em><span class="step-name">見学</span></div>
  <p>事業所の様子をご覧頂き、スタッフとお話ししましょう。</p>
</div>
<div class="abs step" style="top:244px">
  <div class="step-head"><em class="step-no">step.3</em><span class="step-name">体験実習</span></div>
  <p>3日から1週間程度、ご都合に合わせて通って頂きます。</p>
</div>
<div class="abs step" style="top:310px">
  <div class="step-head"><em class="step-no">step.4</em><span class="step-name">利用開始</span></div>
  <p>利用契約を結び、正式に利用開始となります。</p>
</div>

<svg class="abs bulb" width="40" height="48" viewBox="0 0 40 48" aria-hidden="true">
  <circle cx="20" cy="18" r="12" fill="none" stroke="#f2a04a" stroke-width="2.5"/>
  <rect x="14" y="30" width="12" height="8" rx="2" fill="none" stroke="#f2a04a" stroke-width="2.5"/>
  <path d="M4 6 L8 9 M36 6 L32 9 M20 0 V3" stroke="#f2a04a" stroke-width="2"/>
</svg>
<div class="abs before">見学からの体験実習をオススメします。<br>ご自身に合うかどうかを確かめてから<br>ご利用ください。</div>
<h3 class="abs before-title">ご利用開始前に…</h3>

<div class="abs illust family" role="img" aria-label="家族や仲間が集まって楽しく過ごすイラスト"></div>
</body>
</html>
```